Pathlume Background Design

Need to develop a Pathlume Background picture for my profile. The components I want in there are:
1) Name: Mohit Rawal
2) Key Skills: Strategy, Innovation, Execution, Growth and Leadership
3) A photograph (an action photograph) The attached photograph is an example.
A black background would be ideal.

The design should meet the Pathlume background size requirements.

The background should reinforce an image of a thinking person but equally capable of implementing.

Leadership

```html
<!DOCTYPE html>
<html lang="en">
<head>
<meta charset="utf-8">
<title>Mohit Rawal — Pathlume Background</title>
<link rel="stylesheet" href="https://fonts.googleapis.com/css2?family=Open+Sans:wdth,wght@75..100,400..800&display=swap">
<style>
  :root {
    --ink: #000000;
    --paper: #ffffff;
    --name-grey: #7c7c7c;
    --photo-light: #6e6e6e;
    --photo-mid: #3c3c3c;
    --band-shade: #3a3a3a;
  }
  html, body {
    margin: 0;
    padding: 0;
    width: 1200px;
    height: 364px;
    overflow: hidden;
    background: var(--ink);
  }
  .banner {
    display: block;
    width: 1200px;
    height: 364px;
    background: var(--ink);
  }
  .name-primary {
    font-family: "Open Sans", Arial, sans-serif;
    font-weight: 700;
    font-size: 92px;
    fill: var(--paper);
  }
  .name-echo {
    font-family: "Open Sans", Arial, sans-serif;
    font-weight: 700;
    font-size: 148px;
    fill: var(--name-grey);
    stroke: var(--ink);
    stroke-width: 3px;
    paint-order: stroke;
  }
  .skill-label {
    font-family: "Open Sans", "Arial Narrow", sans-serif;
    font-weight: 700;
    font-stretch: 75%;
    font-variation-settings: "wdth" 75;
    font-size: 26px;
    fill: var(--ink);
  }
  .rule { fill: var(--paper); }
</style>
</head>
<body>
<svg class="banner" viewBox="0 0 1200 364" xmlns="http://www.w3.org/2000/svg">
  <defs>
    <radialGradient id="photo-tone" cx="0.4" cy="0.55" r="0.65">
      <stop offset="0" stop-color="var(--photo-light)"/>
      <stop offset="0.55" stop-color="var(--photo-mid)"/>
      <stop offset="1" stop-color="var(--ink)"/>
    </radialGradient>
    <linearGradient id="band-fade" x1="0" y1="0" x2="1" y2="0">
      <stop offset="0" stop-color="var(--band-shade)"/>
      <stop offset="0.28" stop-color="var(--paper)"/>
      <stop offset="1" stop-color="var(--paper)"/>
    </linearGradient>
    <linearGradient id="rule-fade" x1="0" y1="0" x2="1" y2="0">
      <stop offset="0" stop-color="var(--paper)" stop-opacity="0"/>
      <stop offset="0.25" stop-color="var(--paper)"/>
      <stop offset="1" stop-color="var(--paper)"/>
    </linearGradient>
  </defs>

  <rect class="portrait" role="img" aria-label="Black-and-white action photograph of Mohit Rawal in a blazer, pointing upward"
        x="0" y="0" width="370" height="364" fill="url(#photo-tone)"/>

  <text class="name-primary" x="998" y="112" text-anchor="end" textLength="536" lengthAdjust="spacingAndGlyphs">Mohit RAWAL</text>
  <rect class="rule" x="793" y="146" width="236" height="4" fill="url(#rule-fade)"/>
  <text class="name-echo" x="994" y="328" text-anchor="end" textLength="794" lengthAdjust="spacingAndGlyphs">Mohit RAWAL</text>

  <g class="skills">
    <rect x="1030" y="6" width="170" height="60" fill="url(#band-fade)"/>
    <rect x="1030" y="72" width="170" height="3" fill="url(#band-fade)"/>
    <rect x="1030" y="80" width="170" height="58" fill="url(#band-fade)"/>
    <rect x="1030" y="143" width="170" height="3" fill="url(#band-fade)"/>
    <rect x="1030" y="150" width="170" height="60" fill="url(#band-fade)"/>
    <rect x="1030" y="215" width="170" height="3" fill="url(#band-fade)"/>
    <rect x="1030" y="220" width="170" height="60" fill="url(#band-fade)"/>
    <rect x="1030" y="284" width="170" height="3" fill="url(#band-fade)"/>
    <rect x="1030" y="290" width="170" height="64" fill="url(#band-fade)"/>

    <text class="skill-label" x="1188" y="44" text-anchor="end">strategy</text>
    <text class="skill-label" x="1188" y="116" text-anchor="end">execution</text>
    <text class="skill-label" x="1188" y="189" text-anchor="end">innovation</text>
    <text class="skill-label" x="1188" y="258" text-anchor="end">growth</text>
    <text class="skill-label" x="1188" y="328" text-anchor="end">leadership</text>
  </g>
</svg>
</body>
</html>
```